VMR business card

Need a business card for a company that provides instructional design and elearning development services. The website is here: http://vantmoro.studio/

I'm attaching a current logo, as well as the old business card design. While I like to keep it clean, the old design is too simplistic for my liking. The only idea I want to reuse from the old design is placing industry jargon on the back of the card, just need a better way to present it. But if you have other ideas for the back--feel free to experiment.

Please use the colors complementary to the color we have on the website. Thank you!

```html
<!DOCTYPE html>
<html lang="en">
<head>
<meta charset="utf-8">
<title>VMR Business Card</title>
<link rel="stylesheet" href="https://fonts.googleapis.com/css2?family=Roboto:wght@400;500;700&display=swap">
<style>
  :root {
    --backdrop: #a9a7a7;
    --card-dark: #303031;
    --card-light: #f7f7f6;
    --gold: #d6cd88;
    --teal: #1bb5a1;
    --ink: #222324;
    --ink-soft: #3a3b3c;
    --divider: #e2e2e2;
  }
  * { margin: 0; padding: 0; box-sizing: border-box; }
  html, body { width: 1200px; height: 1200px; overflow: hidden; }
  body { background: var(--backdrop); position: relative; font-family: "Roboto", Arial, sans-serif; }

  .card { position: absolute; width: 712px; height: 419px; border-radius: 30px; overflow: hidden; }

  /* Back side */
  .card-back { left: 238px; top: 118px; background: var(--card-dark); }
  .tagline-art {
    position: absolute; left: 172px; top: 96px; width: 370px; height: 226px;
    border-radius: 18px;
    background: linear-gradient(135deg, rgba(214, 205, 136, 0.55) 0%, rgba(168, 168, 170, 0.35) 50%, rgba(27, 181, 161, 0.55) 100%);
  }

  /* Front side */
  .card-front { left: 231px; top: 645px; background: var(--card-light); }
  .brand { position: absolute; left: 92px; top: 168px; display: flex; align-items: center; gap: 16px; }
  .brand-dot { width: 30px; height: 30px; border-radius: 50%; background: var(--gold); }
  .brand-name { font-weight: 700; font-size: 66px; color: var(--teal); letter-spacing: 2px; line-height: 1; }
  .divider { position: absolute; left: 362px; top: 60px; width: 1px; height: 262px; background: var(--divider); }

  .contact { position: absolute; left: 397px; top: 114px; }
  .person-name { font-size: 22px; font-weight: 700; color: var(--ink); letter-spacing: 0.3px; }
  .person-role { font-size: 16px; color: var(--ink-soft); margin-top: 6px; }
  .contact-list { list-style: none; margin-top: 36px; }
  .contact-item { display: flex; align-items: center; gap: 16px; font-size: 18px; color: var(--ink); height: 28px; }
  .contact-item svg { width: 18px; height: 18px; flex: none; margin-left: 1px; }

  .footer-bands { position: absolute; left: 0; bottom: 0; width: 712px; height: 56px; }
  .email { position: absolute; right: 41px; bottom: 18px; font-size: 18px; color: #ffffff; letter-spacing: 0.2px; }
</style>
</head>
<body>

<section class="card card-back" aria-label="Card back">
  <div class="tagline-art" role="img" aria-label="Lettered tagline asking how the studio can help"></div>
</section>

<section class="card card-front" aria-label="Card front">
  <div class="brand">
    <span class="brand-dot"></span>
    <span class="brand-name">VMR</span>
  </div>

  <div class="divider"></div>

  <div class="contact">
    <p class="person-name">Daniel Marsh</p>
    <p class="person-role">Managing Director</p>
    <ul class="contact-list">
      <li class="contact-item">
        <svg viewBox="0 0 20 20" aria-hidden="true"><path fill="var(--teal)" d="M2 7c0-2 3-4 8-4s8 2 8 4v1.5h-4V6.5H6v2H2zM5 9.5h10l2 7H3z"/><circle cx="10" cy="13" r="2" fill="var(--card-light)"/></svg>
        <span>555-014-2287</span>
      </li>
      <li class="contact-item">
        <svg viewBox="0 0 20 20" aria-hidden="true"><circle cx="10" cy="10" r="8" fill="var(--teal)"/><path d="M2 10h16M10 2c-3 3-3 13 0 16M10 2c3 3 3 13 0 16M4 5.5h12M4 14.5h12" stroke="var(--card-light)" stroke-width="1" fill="none"/></svg>
        <span>www.vantmoro.studio</span>
      </li>
    </ul>
  </div>

  <svg class="footer-bands" viewBox="0 0 712 56" aria-hidden="true">
    <rect x="0" y="27" width="340" height="29" fill="var(--gold)"/>
    <polygon points="348,0 712,0 712,56 314,56" fill="var(--teal)"/>
  </svg>
  <span class="email">dmarsh@vantmoro.studio</span>
</section>

</body>
</html>
```